We need a modern WIX website for Brightform Beam Restoration Australia (Laser/Industrial/Engineering)

We need a website for Wix (coded) for our laser restoration and industrial cleaning business.

It will need to be 4-6 pages.
Pages may include:
Home
About
Why Laser
Capabilities
There needs to be a contact / quote form

We do not want boring institutional design, so please do try to be a little creative (but not artsy, more engineering / laser etc). We hesitate with boxy wordpress looking templates, so please bring in strip backgrounds and sliders etc;

Our brand colours are blue and red, but a sharp modern site relative to the industry and work is important.

We envision the home page to take visitors on a informed journey of who, what, why, how, explaining the capability of laser science across contaminants, industries and surfaces.

We envision the home page to be strips:
- landing
- intro

-Why choose laser / What is laser cleaning
Minimum downtime, no surface damage, no environmental impact, no mess, no waste, complete restoration (we have an explainer video)

- Contaminants
Bacteria, Rust, Corrosion, Oxides, Grease, Oil, Paint, Stains, Mold, Soot / Carbon, Graffiti, Coatings, Dirt, Residue

- Surfaces
Metals, Engines/Parts/Components, Tools, Machinery, Bricks/Blockwork, Concrete, Paint, Stone, Wood, Aluminium

- Industries
Medical/Sterile, Hospitality, Bio Hazardous, Construction, Infrastructure, Property, Industrial, Engineer, Automotive, Marine, Heritage, Non Destructive Testing,

----
Here is some info on the company below:

"Background Information - Brightform Beam Restoration Australia (BBRA) is a leading provider of advanced laser restoration services for the residential, commercial, medical, hazardous and industrial sectors, offering waste free, chemical free and damage free complete restoration of metals, concrete, wood, stone and heritage, hygiene and hazard surfaces, with complete removal of coatings, bacteria, paint, rust, graffiti, mold and fire ash (soot), and preparation and treating for welding and bonding.
Servicing Melbourne and Victoria, with additional services available Australia wide, BBRA offers a 24/7 call-out service to your site.
With no downtime to your operations, we offer a timely resolution to your cleaning and maintenance needs."

We have attached some inspiration of websites we like the flow/feel of, but feel free to put your best designs forward.

You are welcome to use dummy headers and text at this stage, as design and feel is most important, and we can add text later.

```html
<!DOCTYPE html>
<html lang="en">
<head>
<meta charset="utf-8">
<title>BBRA – Brightform Beam Restoration Australia</title>
<link href="https://fonts.googleapis.com/css2?family=Montserrat:wght@400;500;600;700&display=swap" rel="stylesheet">
<style>
:root{
  --blue:#1476c0;
  --blue-deep:#0f63a8;
  --blue-light:#3d8fd6;
  --lavender:#9b9ce8;
  --red:#e8212b;
  --ink:#2e2e2e;
  --grey:#7a7a7a;
  --white:#ffffff;
}
*{box-sizing:border-box;margin:0;padding:0}
html,body{width:1200px;height:3125px;overflow:hidden;background:var(--white)}
body{font-family:'Montserrat',sans-serif;color:var(--ink);position:relative}
.abs{position:absolute}

/* header */
.brand{left:142px;top:40px}
.brand-name{display:flex;align-items:center;gap:10px;font-weight:700;font-size:52px;line-height:1;color:var(--red);letter-spacing:2px}
.brand-dot{width:30px;height:30px;border-radius:50%;background:var(--blue)}
.brand-sub{font-size:10.5px;color:var(--blue);font-weight:500;margin-top:6px}
.nav{top:99px;left:639px;display:flex;gap:18px;font-size:13px;font-weight:500;color:var(--red)}
.nav a{color:inherit;text-decoration:none;padding-bottom:5px}
.nav a.active{border-bottom:2px solid var(--red)}

.hero-visual{left:461px;top:0;width:739px;height:600px}
.hero-title{left:143px;top:324px;font-size:40px;font-weight:500;line-height:45px;color:var(--ink)}
.hero-sub{left:141px;top:425px;font-size:20px;line-height:25px;color:var(--grey)}
.btn{display:flex;align-items:center;justify-content:center;font-size:13px;font-weight:500;border-radius:3px;text-decoration:none}
.btn-solid{background:var(--blue);color:var(--white);box-shadow:0 6px 14px rgba(20,118,192,.3)}
.btn-ghost{background:var(--white);color:var(--red);box-shadow:0 4px 14px rgba(0,0,0,.15)}

/* about */
.about-tile{left:142px;top:719px;width:131px;height:215px;background:var(--blue);border-radius:4px;color:var(--white);font-size:23px;font-weight:500;line-height:30px;padding:18px 20px}
.photo{border-radius:2px}
.about-head{left:548px;top:720px;width:480px;font-size:23px;font-weight:500;line-height:25px;color:var(--ink)}
.about-text{left:550px;top:828px;width:465px;font-size:14.5px;line-height:17.5px;color:var(--grey)}

/* how it works */
.eyebrow{width:1200px;left:0;text-align:center;font-size:15px;font-weight:500;color:var(--blue)}
.section-title{width:1200px;left:0;text-align:center;font-size:23px;font-weight:500;color:var(--ink)}
.steps{left:0;top:1220px;width:1200px;height:250px}
.step-label{text-align:center;font-size:15.5px;line-height:18px;font-weight:500;color:var(--ink);width:180px}
.how-text{left:200px;width:800px;text-align:center;font-size:15.5px;line-height:17.6px;color:var(--grey)}

/* why band */
.band-shape{left:0;top:1560px;width:1070px;height:545px}
.why-title{left:237px;top:1793px;font-size:24px;font-weight:500;color:var(--white)}
.why-list{left:204px;top:1850px;list-style:none;color:var(--white);font-size:16px}
.why-list li{height:32.6px;display:flex;align-items:center;gap:14px}
.video{left:705px;top:1809px;width:411px;height:256px;background:#000}
.video-frame{position:absolute;left:0;top:12px;width:411px;height:232px;background:linear-gradient(120deg,#5e5e5e,#b9b9b9 45%,#8a8a8a 60%,#474747)}
.play{position:absolute;left:160px;top:83px}

/* cleaning */
.industries{left:136px;top:2321px;width:237px;height:315px;border-radius:6px 6px 55px 6px;background:linear-gradient(90deg,var(--blue-deep),var(--lavender));color:var(--white);padding:14px 17px}
.card-title{font-size:18px;font-weight:500}
.industries hr{border:none;border-top:1px solid rgba(255,255,255,.45);margin:10px 0 20px}
.card-list{font-size:14.5px;line-height:17.6px;font-weight:500}
.contaminants{left:440px;top:2330px;width:330px;height:310px}
.surface-title{left:825px;top:2323px;width:238px;height:44px;border:1.5px solid var(--blue);box-shadow:0 3px 8px rgba(0,0,0,.12);font-size:18px;font-weight:500;padding:8px 15px}
.surface-body{left:825px;top:2372px;width:238px;height:264px;border:1.5px solid var(--blue);box-shadow:0 3px 8px rgba(0,0,0,.12);overflow:hidden;padding:26px 0 0 15px;color:var(--ink)}
.surface-corner{position:absolute;right:0;bottom:0}

/* footer */
.footer{left:0;top:2760px;width:1200px;height:365px;background:linear-gradient(180deg,#1a72bb,#2680c5 50%,#1b6db3)}
.footer-brand{left:0;width:1200px;top:2812px;text-align:center}
.footer-brand .brand-name{justify-content:center;font-size:48px}
.footer-brand .brand-sub{color:var(--white)}
.footer-nav{left:0;width:1200px;top:2902px;display:flex;justify-content:center;gap:18px;font-size:13px;font-weight:500;color:var(--white)}
.footer-nav a{color:inherit;text-decoration:none}
.footer-nav a.active{color:var(--red)}
.copyright{left:0;width:1200px;top:3070px;text-align:center;color:var(--white);font-size:13px;font-weight:500}
</style>
</head>
<body>

<!-- header -->
<div class="abs brand">
  <div class="brand-name"><span class="brand-dot"></span>BBRA</div>
  <div class="brand-sub">BRIGHTFORM BEAM RESTORATION AUSTRALIA</div>
</div>

<svg class="abs hero-visual" viewBox="0 0 739 600" role="img" aria-label="Photo of a handheld laser cleaning gun">
  <defs>
    <linearGradient id="heroGrad" x1="0" y1="0" x2="1" y2="1">
      <stop offset="0" stop-color="#2e86e0"/>
      <stop offset=".45" stop-color="#7c8ec8"/>
      <stop offset=".7" stop-color="#c9cfe0"/>
      <stop offset="1" stop-color="#eef0f5"/>
    </linearGradient>
  </defs>
  <rect x="120" y="-230" width="620" height="620" rx="60" transform="rotate(45 430 80)" fill="url(#heroGrad)"/>
</svg>

<nav class="abs nav">
  <a class="active" href="#">HOME</a><a href="#">ABOUT US</a><a href="#">WHY LASER</a><a href="#">CAPABILITIES</a><a href="#">CONTACT US</a>
</nav>

<h1 class="abs hero-title">Advanced laser<br>restoration services</h1>
<p class="abs hero-sub">for the residential, commercial, medical,<br>hazardous and industrial sectors</p>
<a class="abs btn btn-solid" style="left:142px;top:518px;width:187px;height:45px" href="#">CONTACT US</a>
<a class="abs btn btn-ghost" style="left:358px;top:518px;width:187px;height:45px" href="#">GET A QUOTE</a>

<!-- about -->
<div class="abs about-tile">About<br>Us</div>
<div class="abs photo" style="left:277px;top:719px;width:217px;height:215px;background:linear-gradient(135deg,#3a7fd0,#d7dce4 55%,#2d6cc0)" role="img" aria-label="Photo of a laser cleaning machine"></div>
<div class="abs photo" style="left:142px;top:940px;width:352px;height:106px;background:linear-gradient(90deg,#3a3f48,#8a8f98 40%,#c46a3a 55%,#4a4f58)" role="img" aria-label="Photo of a laser beam cleaning a metal surface"></div>

<h2 class="abs about-head">&nbsp;Brightform Beam Restoration Australia (BBRA) is a leading provider of advanced laser restoration services.</h2>
<p class="abs about-text">BBRA is a leading provider of advanced laser restoration services for the residential, commercial, medical, hazardous and industrial sectors, offering waste free, chemical free and damage free complete restoration of metals, concrete, wood, stone and heritage, hygiene and hazard surfaces, with complete removal of coatings, bacteria, paint, rust, graffiti, mold and fire ash (soot), and preparation and treating for welding and bonding.</p>
<a class="abs btn btn-ghost" style="left:682px;top:993px;width:188px;height:45px" href="#">READ MORE</a>

<!-- how it works -->
<div class="abs eyebrow" style="top:1126px">HOW IT WORKS</div>
<h2 class="abs section-title" style="top:1153px">What is laser cleaning</h2>

<svg class="abs steps" viewBox="0 1220 1200 250">
  <defs>
    <linearGradient id="arcGrad" x1="0" y1="0" x2="1" y2="0">
      <stop offset="0" stop-color="#1476c0"/><stop offset="1" stop-color="#9b9ce8"/>
    </linearGradient>
    <filter id="soft" x="-30%" y="-30%" width="160%" height="160%"><feDropShadow dx="0" dy="3" stdDeviation="5" flood-opacity=".15"/></filter>
  </defs>
  <g fill="none" stroke="url(#arcGrad)" stroke-width="3.5">
    <path d="M302 1308 A75 75 0 0 1 452 1308"/>
    <path d="M452 1344 A75 75 0 0 0 602 1344"/>
    <path d="M601 1307 A75 75 0 0 1 751 1307"/>
    <path d="M750 1343 A75 75 0 0 0 900 1343"/>
  </g>
  <g fill="#fff" filter="url(#soft)">
    <circle cx="377" cy="1308" r="57"/><circle cx="527" cy="1344" r="57"/>
    <circle cx="676" cy="1307" r="57"/><circle cx="825" cy="1343" r="57"/>
  </g>
  <circle cx="377" cy="1308" r="26" fill="#f7e96a" opacity=".7" role="img" aria-label="Illustration of a laser pulse"/>
  <circle cx="527" cy="1344" r="26" fill="#1476c0" opacity=".25" role="img" aria-label="Illustration of a contaminated surface grid"/>
  <circle cx="676" cy="1307" r="26" fill="#3d8fd6" opacity=".3" role="img" aria-label="Illustration of contaminants absorbing light"/>
  <circle cx="825" cy="1343" r="26" fill="#9b9ce8" opacity=".35" role="img" aria-label="Illustration of contaminants turning into gas"/>
  <g fill="#1476c0"><circle cx="303" cy="1309" r="11"/><circle cx="453" cy="1339" r="11"/><circle cx="603" cy="1311" r="11"/><circle cx="752" cy="1341" r="11"/></g>
  <g fill="#fff" font-family="Montserrat, sans-serif" font-size="12" font-weight="700" text-anchor="middle">
    <text x="303" y="1313">1.</text><text x="453" y="1343">2.</text><text x="603" y="1315">3.</text><text x="752" y="1345">4.</text>
  </g>
</svg>
<div class="abs step-label" style="left:287px;top:1382px">Nanosecond-length pulses of laser light</div>
<div class="abs step-label" style="left:440px;top:1421px">Contaminated surface</div>
<div class="abs step-label" style="left:583px;top:1379px">Contaminants absorb laser light</div>
<div class="abs step-label" style="left:739px;top:1421px">The contaminants will turn into a gas</div>

<p class="abs how-text" style="top:1508px">Laser cleaning technology works by sending nanosecond-length pulses of laser light towards a surface. When it interacts with contaminants that absorb laser light, the contaminants or coating particles will either turn into a gas or the pressure of the interaction will cause particles to free from the surface.</p>
<p class="abs how-text" style="top:1578px">With the right laser settings and equipment, laser cleaning is unmatched in its ability to clean all the way to the bare metal of your product. Keenedge Laser specializes in the know-how and application of laser cleaning solutions to put together the formula for your specific situation. Once we identify the combination of settings and equipment, the process can be matched across other setups – working very efficiently without affecting the integrity of the surface you are cleaning.</p>

<!-- why choose laser -->
<svg class="abs band-shape" viewBox="0 1560 1070 545">
  <path d="M0 1560 A157 179 0 0 0 157 1739 L1070 1739 L1070 2105 L0 2105 Z" fill="var(--blue)"/>
</svg>
<h2 class="abs why-title">Why choose laser</h2>
<ul class="abs why-list">
  <li><svg width="20" height="20" viewBox="0 0 20 20"><path d="M14 5 A7 7 0 1 0 14 15" fill="none" stroke="var(--red)" stroke-width="3"/><circle cx="10" cy="10" r="2.5" fill="var(--red)"/></svg>minimum downtime</li>
  <li><svg width="20" height="20" viewBox="0 0 20 20"><path d="M14 5 A7 7 0 1 0 14 15" fill="none" stroke="var(--red)" stroke-width="3"/><circle cx="10" cy="10" r="2.5" fill="var(--red)"/></svg>no surface damage</li>
  <li><svg width="20" height="20" viewBox="0 0 20 20"><path d="M14 5 A7 7 0 1 0 14 15" fill="none" stroke="var(--red)" stroke-width="3"/><circle cx="10" cy="10" r="2.5" fill="var(--red)"/></svg>no environmental impact</li>
  <li><svg width="20" height="20" viewBox="0 0 20 20"><path d="M14 5 A7 7 0 1 0 14 15" fill="none" stroke="var(--red)" stroke-width="3"/><circle cx="10" cy="10" r="2.5" fill="var(--red)"/></svg>no mess,</li>
  <li><svg width="20" height="20" viewBox="0 0 20 20"><path d="M14 5 A7 7 0 1 0 14 15" fill="none" stroke="var(--red)" stroke-width="3"/><circle cx="10" cy="10" r="2.5" fill="var(--red)"/></svg>no waste,</li>
  <li><svg width="20" height="20" viewBox="0 0 20 20"><path d="M14 5 A7 7 0 1 0 14 15" fill="none" stroke="var(--red)" stroke-width="3"/><circle cx="10" cy="10" r="2.5" fill="var(--red)"/></svg>complete restoration</li>
</ul>
<div class="abs video">
  <div class="video-frame" role="img" aria-label="Explainer video still of a laser head cleaning a steel plate"></div>
  <svg class="play" width="90" height="90" viewBox="0 0 90 90">
    <circle cx="45" cy="45" r="40" fill="rgba(255,255,255,.15)" stroke="var(--blue-light)" stroke-width="6"/>
    <path d="M36 28 L62 45 L36 62 Z" fill="var(--white)"/>
  </svg>
</div>

<!-- what we are cleaning -->
<div class="abs eyebrow" style="top:2188px;left:-7px">COMPETENCIES</div>
<h2 class="abs section-title" style="top:2215px;left:-7px">What we are cleaning</h2>

<div class="abs industries">
  <div class="card-title">Industries</div>
  <hr>
  <div class="card-list">Medical/Sterile,<br>Hospitality,<br>Bio Hazardous,<br>Construction,<br>Infrastructure,<br>Property,<br>Industrial,<br>Engineer,<br>Automotive,<br>Marine,<br>Heritage,<br>Non Destructive Testing</div>
</div>

<svg class="abs contaminants" viewBox="440 2330 330 310" font-family="Montserrat, sans-serif">
  <defs>
    <radialGradient id="hexGlow"><stop offset=".6" stop-color="#fff"/><stop offset="1" stop-color="#cfe2f5"/></radialGradient>
  </defs>
  <circle cx="603" cy="2482" r="92" fill="url(#hexGlow)" stroke="var(--blue)" stroke-width="4"/>
  <text x="603" y="2489" text-anchor="middle" font-size="18" font-weight="500" fill="#2e2e2e">Contaminants</text>
  <circle cx="545" cy="2383" r="36" fill="#3a9bb8" role="img" aria-label="Photo of bacteria"/>
  <circle cx="655" cy="2387" r="36" fill="#8a3d22" role="img" aria-label="Photo of rust"/>
  <circle cx="491" cy="2482" r="36" fill="#2a2a2a" role="img" aria-label="Photo of grease"/>
  <circle cx="712" cy="2486" r="36" fill="#6f86a8" role="img" aria-label="Photo of oil"/>
  <circle cx="539" cy="2573" r="36" fill="#8b7468" role="img" aria-label="Photo of oxides"/>
  <circle cx="655" cy="2575" r="36" fill="#a4501c" role="img" aria-label="Photo of corrosion"/>
  <g font-size="15.5" font-weight="500" fill="#2e2e2e" text-anchor="middle">
    <text x="545" y="2352">Bacteria</text><text x="655" y="2352">Rust</text>
    <text x="490" y="2445">Grease</text><text x="713" y="2445">Oil</text>
    <text x="537" y="2627">Oxides</text><text x="656" y="2627">Corrosion</text>
  </g>
</svg>

<div class="abs surface-title">Surfaces</div>
<div class="abs surface-body">
  <div class="card-list">Metals,<br>Engines/Parts/Components,<br>Tools,<br>Machinery,<br>Bricks/Blockwork,<br>Concrete,<br>Paint,<br>Stone,<br>Wood,<br>Aluminium</div>
  <svg class="surface-corner" width="65" height="58" viewBox="0 0 65 58">
    <defs><linearGradient id="cornerGrad" x1="0" y1="1" x2="1" y2="0"><stop offset="0" stop-color="#9b9ce8"/><stop offset="1" stop-color="#1476c0"/></linearGradient></defs>
    <path d="M65 0 L65 58 L0 58 Z" fill="url(#cornerGrad)"/>
  </svg>
</div>

<!-- footer -->
<div class="abs footer" role="img" aria-label="Blue tinted photo of a laser cleaned metal surface"></div>
<div class="abs footer-brand">
  <div class="brand-name"><span class="brand-dot" style="background:var(--white)"></span>BBRA</div>
  <div class="brand-sub">BRIGHTFORM BEAM RESTORATION AUSTRALIA</div>
</div>
<nav class="abs footer-nav">
  <a class="active" href="#">HOME</a><a href="#">ABOUT US</a><a href="#">WHY LASER</a><a href="#">CAPABILITIES</a><a href="#">CONTACT US</a>
</nav>
<a class="abs btn btn-ghost" style="left:506px;top:2969px;width:187px;height:45px" href="#">CONTACT US</a>
<div class="abs copyright">Copyright © 2023 BBRA</div>

</body>
</html>
```